Website design for luxury private hair salon

I'm looking for someone to use my Logo and build me a website for my webpage www.lunetresses.com.au (You can have a look at it as it has every detail I need included on it already), however I want a fresh new appearance and it to look and feel super stylish.

I am thinking colours in black, with silver or white, beautiful hair images like the ones you'll see on the current webpage - the price list as per what you already see.

I will include a copy of my biz card on here, so you can see the feel of the card, and design a website with a similar feel. It is matt black with a foil silver.

Modern, but classic and fresh. I will also need you to be able to publish it to my URL for me as I have no idea how to do this. I need it up and running pronto!

The website will need to be able to be read clearly on all devices incluing smart phones and ipads. The URL is currently registered and hosted by Nimbo Vault

Thinking a Home Page - large logo etc and write up on who and what we offer
Services/Price List page - as per the price list on my current webpage
Contact Page - with a built in contact form.

Target Market(s)

Middle aged, fashionable, stylish women and men who enjoy luxury hair care and styling in an upmarket location.

Industry/Entity Type

Hair And Beauty

Number of Pages Required

3 page

Font styles to use
Other font styles liked:
• see my images for my current logo

Colors
000000
b2b2b2
a54499

Requirements
Must have
• Style
• Fast turnaround
• Be viewable on all devices, PC, ipads, smart phones
• Designer able to upload it so its a running website for me to my URL
Nice to have
• Just a really feminine, stylish website which is easy to read and shows some beautiful images of perfect hair
Should not have
• Browns, reds or orange colours.

```html
<!DOCTYPE html>
<html lang="en">
<head>
<meta charset="utf-8">
<title>Lune Tresses hair &amp; body</title>
<link rel="stylesheet" href="https://fonts.googleapis.com/css2?family=Nunito+Sans:wght@300;400;600;700&family=Open+Sans:wght@400;600&display=swap">
<style>
:root{
  --purple:#a54499;
  --ink:#222222;
  --band:#242424;
  --grey:#b2b2b2;
  --text:#666666;
  --muted:#8a8a8a;
  --icon:#444444;
  --white:#ffffff;
  --head:"Nunito Sans", Arial, sans-serif;
  --body:"Open Sans", Arial, sans-serif;
}
*{box-sizing:border-box;margin:0;padding:0}
html,body{width:1200px;height:2161px;overflow:hidden;background:var(--white)}
body{position:relative;font-family:var(--body);color:var(--text)}
.abs{position:absolute}

/* header */
.brand{left:132px;top:42px;width:270px;color:#8c8f99;font-family:var(--head);font-weight:300;white-space:nowrap}
.brand-name{display:block;font-size:50px;line-height:1;letter-spacing:1px}
.brand-tag{display:block;font-size:20px;line-height:1;letter-spacing:3px;margin-top:12px;text-align:right;padding-right:8px}
.phones{top:60px;right:133px;display:flex;align-items:center;font-family:var(--head);color:#555;font-size:18px;text-align:right;line-height:1.15}
.phone-block{padding:0 18px}
.phone-block:first-child{padding-left:0}
.phone-divider{width:1px;height:40px;background:#ddd}
.phone-icon{margin-left:10px}
.main-nav{top:140px;right:133px;display:flex;gap:35px;font-family:var(--head);font-size:15.5px;color:#555}
.main-nav .active{color:var(--purple)}

/* hero */
.hero{left:0;top:192px;width:1200px;height:422px;background:linear-gradient(100deg,#cfc2a8 0%,#e6d49f 35%,#d9c6a0 55%,#cfc3b3 75%,#c9bcac 100%)}
.slide-arrow{width:29px;height:29px;background:#777;opacity:.75;display:flex;align-items:center;justify-content:center}

/* sections */
.section-title{left:0;width:1200px;text-align:center;font-family:var(--head);font-weight:600;color:var(--purple);font-size:32px;letter-spacing:.5px}
.intro{left:140px;width:920px;top:716px;text-align:center;font-size:14.5px;line-height:22px;color:var(--text)}
.gallery{left:0;top:820px;width:1200px;height:279px;display:flex}
.gallery-photo{width:400px;height:279px}
.g1{background:linear-gradient(90deg,#b8a58a,#9d9284 60%,#8a8478)}
.g2{background:radial-gradient(circle at 50% 45%,#d9c98f 0%,#6f6550 30%,#1d1c17 70%)}
.g3{background:linear-gradient(90deg,#c8b3a5,#b0604a 45%,#cfb8ad)}

.services{left:120px;top:1240px;width:960px;display:grid;grid-template-columns:repeat(4,232px);column-gap:10px;row-gap:40px;justify-content:space-between}
.service{text-align:center}
.service svg{display:block;margin:0 auto;height:52px}
.service-name{font-family:var(--head);font-size:21px;color:#333;margin-top:21px}
.service-desc{font-size:10.5px;line-height:16px;color:var(--muted);margin-top:6px;padding:0 14px}

/* booking */
.booking{left:0;top:1652px;width:1200px;height:385px;background:var(--band);color:var(--white)}
.booking-title{position:absolute;top:74px;width:100%;text-align:center;font-family:var(--head);font-weight:600;font-size:32px;letter-spacing:.5px}
.booking-form{position:absolute;top:130px;left:205px;display:flex;gap:16px}
.field{width:220px;height:38px;background:var(--white);color:#666;font-size:13px;display:flex;align-items:center;justify-content:space-between;padding:0 14px}
.submit{width:79px;height:38px;background:var(--purple);color:var(--white);font-family:var(--head);font-weight:700;font-size:13px;display:flex;align-items:center;justify-content:center}
.booking-note{position:absolute;width:100%;text-align:center;font-family:var(--head);font-size:17px;color:#aaa}
.contact-row{position:absolute;top:285px;left:132px;width:936px;display:flex;justify-content:space-between;font-family:var(--head);font-size:15px;white-space:nowrap}
.contact-row span{display:flex;align-items:center;gap:8px}

/* footer */
.footer-nav{left:132px;top:2075px;font-size:11px;color:#444}
.footer-nav span{margin:0 7px}
.copyright{left:132px;top:2104px;font-size:11px;color:#444}
.social{left:979px;top:2087px;display:flex;gap:8px}
.social i{display:block;width:24px;height:24px;border-radius:50%}
</style>
</head>
<body>

<header>
  <div class="abs brand"><span class="brand-name">Lune Tresses</span><span class="brand-tag">hair &amp; body</span></div>
  <div class="abs phones">
    <div class="phone-block">Cara<br>0491 530 274</div>
    <div class="phone-divider"></div>
    <div class="phone-block">Tess<br>0437 860 915</div>
    <svg class="phone-icon" width="20" height="32" viewBox="0 0 20 32"><rect x="1" y="1" width="18" height="30" rx="3" fill="none" stroke="#999" stroke-width="1.5"/><line x1="2" y1="6" x2="18" y2="6" stroke="#999"/><line x1="2" y1="25" x2="18" y2="25" stroke="#999"/></svg>
  </div>
  <nav class="abs main-nav"><span class="active">Welcome</span><span>Who we are</span><span>What we offer</span><span>Price List</span><span>Contact Us</span></nav>
</header>

<div class="abs hero" role="img" aria-label="Woman in profile with long flowing blonde hair"></div>
<div class="abs slide-arrow" style="left:0;top:388px"><svg width="12" height="12" viewBox="0 0 12 12"><path d="M11 6H2M6 2L2 6l4 4" stroke="#fff" stroke-width="1.6" fill="none"/></svg></div>
<div class="abs slide-arrow" style="right:0;top:388px"><svg width="12" height="12" viewBox="0 0 12 12"><path d="M1 6h9M6 2l4 4-4 4" stroke="#fff" stroke-width="1.6" fill="none"/></svg></div>

<h2 class="abs section-title" style="top:672px">WHO WE ARE</h2>
<p class="abs intro">We pride ourselves on being able to offer a private salon experience to our clients in the exclusive suburb of Marlow Heights, where your hair design and colouring needs will be met with years of experience and current industry training and knowledge</p>

<div class="abs gallery">
  <div class="gallery-photo g1" role="img" aria-label="Woman with long wavy blonde hair by a stone wall"></div>
  <div class="gallery-photo g2" role="img" aria-label="Woman with voluminous blonde curls on a dark background"></div>
  <div class="gallery-photo g3" role="img" aria-label="Woman with long red hair in a denim jacket"></div>
</div>
<div class="abs slide-arrow" style="left:0;top:944px;width:20px"><svg width="10" height="12" viewBox="0 0 10 12"><path d="M8 1L2 6l6 5z" fill="#fff"/></svg></div>
<div class="abs slide-arrow" style="right:0;top:944px;width:20px"><svg width="10" height="12" viewBox="0 0 10 12"><path d="M2 1l6 5-6 5z" fill="#fff"/></svg></div>

<h2 class="abs section-title" style="top:1170px">WHAT WE OFFER</h2>
<div class="abs services">
  <div class="service">
    <svg viewBox="0 0 52 52" width="52"><circle cx="10" cy="36" r="5" fill="none" stroke="var(--icon)" stroke-width="2.5"/><circle cx="17" cy="44" r="5" fill="none" stroke="var(--icon)" stroke-width="2.5"/><path d="M14 33L48 6M20 40L46 12" stroke="var(--icon)" stroke-width="2.5"/></svg>
    <div class="service-name">Hair Cuts</div>
    <p class="service-desc">Phasellus purus elit, ornare sit amet vehic ula cursus, pulvinar sit amet elit. Etiam dignissim purus dolor.</p>
  </div>
  <div class="service">
    <svg viewBox="0 0 52 52" width="52"><path d="M30 20L48 2" stroke="var(--icon)" stroke-width="4"/><path d="M24 16l12 12-6 4-10-10z" fill="var(--icon)"/><path d="M20 22l10 10-16 16-10-10z" fill="var(--icon)"/></svg>
    <div class="service-name">Colouring</div>
    <p class="service-desc">Phasellus purus elit, ornare sit amet vehic ula cursus, pulvinar sit amet elit. Etiam dignissim purus dolor.</p>
  </div>
  <div class="service">
    <svg viewBox="0 0 52 52" width="52"><path d="M6 10v34M12 8v38M18 10v34M24 12v30" stroke="var(--icon)" stroke-width="3.5" stroke-linecap="round"/><path d="M36 30l14-16" stroke="var(--icon)" stroke-width="3"/><path d="M30 28l6 6-4 8-8-8z" fill="var(--icon)"/></svg>
    <div class="service-name">Highlighting</div>
    <p class="service-desc">Phasellus purus elit, ornare sit amet vehic ula cursus, pulvinar sit amet elit. Etiam dignissim purus dolor.</p>
  </div>
  <div class="service">
    <svg viewBox="0 0 52 52" width="52"><rect x="14" y="3" width="24" height="6" rx="2" fill="var(--icon)"/><path d="M18 9c-4 10 4 18 0 28s2 12 0 14M26 9c-4 10 4 18 0 28s2 12 0 14M34 9c-4 10 4 18 0 28s2 12 0 14" stroke="var(--icon)" stroke-width="3" fill="none" stroke-linecap="round"/></svg>
    <div class="service-name">Extensions</div>
    <p class="service-desc">Phasellus purus elit, ornare sit amet vehic ula cursus, pulvinar sit amet elit. Etiam dignissim purus dolor.</p>
  </div>
  <div class="service">
    <svg viewBox="0 0 52 52" width="52"><path d="M4 44L46 6M8 48L50 10" stroke="var(--icon)" stroke-width="4"/></svg>
    <div class="service-name">Straightening</div>
    <p class="service-desc">Phasellus purus elit, ornare sit amet vehic ula cursus, pulvinar sit amet elit. Etiam dignissim purus dolor.</p>
  </div>
  <div class="service">
    <svg viewBox="0 0 52 52" width="52"><circle cx="26" cy="32" r="15" fill="none" stroke="var(--icon)" stroke-width="4"/><path d="M26 4l8 8-8 8-8-8z" fill="var(--icon)"/></svg>
    <div class="service-name">Bridal</div>
    <p class="service-desc">Phasellus purus elit, ornare sit amet vehic ula cursus, pulvinar sit amet elit. Etiam dignissim purus dolor.</p>
  </div>
  <div class="service">
    <svg viewBox="0 0 52 52" width="52"><path d="M16 2h16v8H16z" fill="var(--icon)"/><path d="M32 4h10l-4 4h-6z" fill="var(--icon)"/><rect x="20" y="10" width="8" height="8" fill="var(--icon)"/><path d="M17 18h14l6 10v20H11V28z" fill="var(--icon)"/></svg>
    <div class="service-name">Treatments</div>
    <p class="service-desc">Phasellus purus elit, ornare sit amet vehic ula cursus, pulvinar sit amet elit. Etiam dignissim purus dolor.</p>
  </div>
  <div class="service">
    <svg viewBox="0 0 52 52" width="52"><path d="M16 2h20v4l-4 36h-12L16 6z" fill="none" stroke="var(--icon)" stroke-width="2.5"/><rect x="20" y="42" width="12" height="8" fill="var(--icon)"/></svg>
    <div class="service-name">Products &amp; Advice</div>
    <p class="service-desc">Phasellus purus elit, ornare sit amet vehic ula cursus, pulvinar sit amet elit. Etiam dignissim purus dolor.</p>
  </div>
</div>

<section class="abs booking">
  <h2 class="booking-title">BOOK AN APPOINTMENT</h2>
  <div class="booking-form">
    <div class="field">Date <svg width="12" height="12" viewBox="0 0 12 12"><rect x="1" y="2" width="10" height="9" fill="none" stroke="#555"/><path d="M1 5h10" stroke="#555"/></svg></div>
    <div class="field">Time <svg width="12" height="12" viewBox="0 0 12 12"><circle cx="6" cy="6" r="5" fill="none" stroke="#555" stroke-width="1.4"/><path d="M6 3v3h2" stroke="#555" fill="none"/></svg></div>
    <div class="field">For <svg width="10" height="6" viewBox="0 0 10 6"><path d="M1 1l4 4 4-4" stroke="#555" fill="none"/></svg></div>
    <div class="submit">SUBMIT</div>
  </div>
  <p class="booking-note" style="top:206px">If you are unable to make your appointment, please contact us ASAP to reschedule.</p>
  <p class="booking-note" style="top:240px">Thank you!</p>
  <div class="contact-row">
    <span><svg width="10" height="14" viewBox="0 0 10 14"><path d="M5 0a5 5 0 0 1 5 5c0 4-5 9-5 9S0 9 0 5a5 5 0 0 1 5-5z" fill="#fff"/><circle cx="5" cy="5" r="2" fill="var(--band)"/></svg>MARLOW HEIGHTS, Western Australia - 6099</span>
    <span><svg width="8" height="13" viewBox="0 0 8 13"><rect x="0.5" y="0.5" width="7" height="12" rx="1.5" fill="none" stroke="#fff"/></svg>CARA&nbsp; 0491 530 274</span>
    <span><svg width="8" height="13" viewBox="0 0 8 13"><rect x="0.5" y="0.5" width="7" height="12" rx="1.5" fill="none" stroke="#fff"/></svg>TESS&nbsp; 0437 860 915</span>
    <span><svg width="14" height="11" viewBox="0 0 14 11"><rect width="14" height="11" fill="#fff"/><path d="M0 0l7 6 7-6" stroke="var(--band)" fill="none"/></svg>hello@lunetresses.com.au</span>
  </div>
</section>

<footer>
  <div class="abs footer-nav">Welcome<span>|</span>Who we are<span>|</span>What we offer<span>|</span>Price List<span>|</span>Contact Us</div>
  <div class="abs copyright">Copyright &copy; 2017 &nbsp; Company name. &nbsp; All rights reserved.</div>
  <div class="abs social"><i style="background:#3b5998"></i><i style="background:#1da1f2"></i><i style="background:#4e7ba3"></i></div>
</footer>

</body>
</html>
```